Package Design - Disposable Face Towel

Hi,

We are needing assistance with graphic design on our box/carton/package.

The attached image that is white is our biggest competitor.

Our brand is "BRIGHT DEW LTD." Please see the logo we uploaded.

Oder we have in mind for front of box:

Logo
LARGE TOWELS
50 Count
Ultra Soft| 100% USDA Bio-Based|100% Eucalyptus Viscose | Vegan
BRIGHTDEWLTD.EXAMPLE

We like medium to dark blue on most of the box, with white and minimal hot pink or salmon. Something that is sharp, modern, and stands out from our competitors.

Box dimensions are: 6.25 x 5.25 x 4.75 inches

This will be 1 of many design projects.

Target Market(s)

Female Beauty Products

Font styles to use
Serif
Sans Serif

Colors
0054AA
0677BA
7BADD7
CADEEF
E8F1F8
EB3D1F
EC4F4E
F09395
F8D3D4
FCEDEE

Requirements
Must have
• Needs to look sharp and modern

```html
<!DOCTYPE html>
<html lang="en">
<head>
<meta charset="utf-8">
<title>Bright Dew Ltd. – Large Towels Carton</title>
<link rel="stylesheet" href="https://fonts.googleapis.com/css2?family=Quicksand:wght@400;500;600&display=swap">
<style>
  :root {
    --navy: #0b2563;
    --navy-pattern: #163687;
    --band-red: #ff2200;
    --white: #ffffff;
    --stage: #e6e6e6;
  }
  * { box-sizing: border-box; margin: 0; padding: 0; }
  html, body {
    width: 1200px; height: 1200px; overflow: hidden;
    background: var(--stage);
    font-family: "Quicksand", sans-serif;
    color: var(--white);
  }
  .carton { position: relative; width: 1200px; height: 1200px; }
  .panel {
    position: absolute; overflow: hidden;
    background: var(--navy);
    border: 1px solid rgba(255,255,255,0.15);
  }
  .pattern { position: absolute; inset: 0; width: 100%; height: 100%; }
  .panel-top   { left: 100px; top: 130px; width: 560px; height: 440px; }
  .panel-front { left: 100px; top: 570px; width: 560px; height: 500px; }
  .panel-side  { left: 660px; top: 570px; width: 440px; height: 500px; }

  .brand-name {
    position: absolute; left: 0; right: 0; text-align: center;
    font-weight: 500; letter-spacing: 0.08em; white-space: nowrap;
  }
  .product-name {
    position: absolute; left: 0; right: 0; text-align: center;
    font-weight: 400; letter-spacing: 0.01em;
  }
  .panel-top .brand-name { top: 150px; font-size: 38px; }
  .panel-top .product-name { top: 210px; font-size: 36px; }

  .panel-front .brand-name { top: 150px; font-size: 40px; }
  .panel-front .product-name { top: 285px; font-size: 40px; }
  .count { position: absolute; left: 0; right: 0; top: 333px; text-align: center; font-size: 26px; }
  .features {
    position: absolute; left: 0; right: 0; top: 372px; text-align: center;
    font-size: 12.5px; font-weight: 500; white-space: nowrap;
  }
  .band {
    position: absolute; left: 0; right: 0; bottom: 0; height: 100px;
    background: var(--band-red);
  }
  .website {
    position: absolute; left: 0; right: 0; top: 38px; text-align: center;
    font-size: 17px; font-weight: 500; letter-spacing: 0.3em;
  }
  .care {
    position: absolute; left: 90px; top: 60px; width: 300px;
    font-size: 13.5px; line-height: 1.65; font-weight: 500;
  }
  .care-title { text-decoration: underline; }
  .care p + p { margin-top: 40px; }
</style>
</head>
<body>
<main class="carton">

  <section class="panel panel-top">
    <svg class="pattern" role="img" aria-label="Tone-on-tone line pattern of leaves and small flowers" preserveAspectRatio="none" viewBox="0 0 10 10">
      <defs><radialGradient id="pt" cx="50%" cy="50%" r="70%"><stop offset="0" stop-color="#163687"/><stop offset="1" stop-color="#0b2563"/></radialGradient></defs>
      <rect width="10" height="10" fill="url(#pt)"/>
    </svg>
    <div class="brand-name">BRIGHT DEW LTD.</div>
    <div class="product-name">LARGE TOWELS</div>
  </section>

  <section class="panel panel-front">
    <svg class="pattern" role="img" aria-label="Tone-on-tone line pattern of leaves and small flowers" preserveAspectRatio="none" viewBox="0 0 10 10">
      <defs><radialGradient id="pf" cx="50%" cy="45%" r="70%"><stop offset="0" stop-color="#163687"/><stop offset="1" stop-color="#0b2563"/></radialGradient></defs>
      <rect width="10" height="10" fill="url(#pf)"/>
    </svg>
    <div class="brand-name">BRIGHT DEW LTD.</div>
    <div class="product-name">LARGE TOWELS</div>
    <div class="count">50 COUNT</div>
    <div class="features">ULTRA SOFT | 100% USDA BIO-BASED | 100% EUCALYPTUS VISCOSE | VEGAN</div>
    <div class="band"><div class="website">BRIGHTDEWLTD.EXAMPLE</div></div>
  </section>

  <section class="panel panel-side">
    <svg class="pattern" role="img" aria-label="Tone-on-tone line pattern of leaves and small flowers" preserveAspectRatio="none" viewBox="0 0 10 10">
      <defs><radialGradient id="ps" cx="50%" cy="45%" r="70%"><stop offset="0" stop-color="#163687"/><stop offset="1" stop-color="#0b2563"/></radialGradient></defs>
      <rect width="10" height="10" fill="url(#ps)"/>
    </svg>
    <div class="care">
      <p><span class="care-title">Care Instructions:</span><br>
      Lorem ipsum dolor sit amet. Sed exerci feugiat augue eu voluptua takimata. Et dolore facilisi aliquyam ipsum lorem consetetur. Amet et gubergren sed dolor. Sed amet sadipscing nonumy dolore sit. Sadipscing dolore rebum nonumy dolore nulla duis gubergren. Sed enim</p>
      <p>Lorem ipsum dolor sit amet. Sed exerci feugiat augue eu voluptua takimata. Et dolore facilisi aliquyam ipsum lorem consetetur. Amet et gubergren sed dolor. Sed amet sadipscing nonumy dolore sit. Sadipscing dolore rebum nonumy dolore nulla duis gubergren. Sed enim</p>
    </div>
    <div class="band"></div>
  </section>

</main>
</body>
</html>
```